HarwickStrategy Business Card Design

Design business cards with attached ideas. I am open to several different ideas that would be interesting and innovative. What I have provided is logo and colors. Font should be Helvetica although it could be bold or light as needed. The design can be vertical or horizontal. The design should be more interesting than a standard business card. Files must be ready to send to a printer and in Illustrator format. The text with the five icons should be exact. Send me some ideas and I will get back to you right away. I need to choose a design within 3-5 days.

Target Market(s)

Business audience

Industry/Entity Type

Business

Contact Information for Business Card

Files should be ready to send to printer in illustrator format

Font styles to use
Sans Serif

Colors
3276b5

Requirements
Must have
• Use attached logo and two colors - blue / gray
• Include 5 offering icons and text on back
Nice to have
• Interesting and innovative design. Vertical or horizontal are both fine.

```html
<!DOCTYPE html>
<html lang="en">
<head>
<meta charset="utf-8">
<title>HarwickStrategy Business Card</title>
<link rel="stylesheet" href="https://fonts.googleapis.com/css2?family=Arimo:wght@400;700&family=Open+Sans:wght@400&display=swap">
<style>
  :root {
    --blue: #3482f0;
    --slate: #3f4b54;
    --paper: #ffffff;
  }
  html, body {
    margin: 0;
    padding: 0;
    width: 1200px;
    height: 667px;
    overflow: hidden;
    background: var(--paper);
  }
  .card {
    position: relative;
    width: 1200px;
    height: 667px;
    background: var(--paper);
    font-family: "Arimo", Helvetica, Arial, sans-serif;
    color: var(--slate);
  }
  .brand-square {
    position: absolute;
    left: 510px;
    top: 97px;
    width: 192px;
    height: 192px;
    border-radius: 12px;
    background: var(--blue);
  }
  .brand-name {
    position: absolute;
    left: 0;
    right: 0;
    top: 303px;
    margin: 0;
    text-align: center;
    font-family: "Arimo", Helvetica, Arial, sans-serif;
    font-weight: 400;
    font-size: 80px;
    line-height: 1;
    letter-spacing: -1px;
    color: var(--slate);
    white-space: nowrap;
  }
  .tagline {
    position: absolute;
    left: 0;
    right: 0;
    top: 398px;
    margin: 0;
    text-align: center;
    font-family: "Open Sans", Helvetica, Arial, sans-serif;
    font-size: 34px;
    line-height: 1;
    color: var(--slate);
    white-space: nowrap;
  }
  .person {
    position: absolute;
    left: 0;
    right: 0;
    top: 502px;
    margin: 0;
    text-align: center;
    font-size: 38px;
    line-height: 1;
    white-space: nowrap;
  }
  .person-first {
    font-weight: 700;
    color: var(--blue);
  }
  .person-last {
    font-weight: 400;
    color: var(--slate);
  }
  .person-degree {
    font-size: 29px;
    color: var(--slate);
  }
  .person-title {
    position: absolute;
    left: 0;
    right: 0;
    top: 545px;
    margin: 0;
    text-align: center;
    font-size: 28px;
    line-height: 1;
    color: var(--slate);
    white-space: nowrap;
  }
</style>
</head>
<body>
  <main class="card">
    <div class="brand-square" aria-hidden="true"></div>
    <h1 class="brand-name">HarwickStrategy</h1>
    <p class="tagline">Clear Plans - Lasting Results</p>
    <p class="person">
      <span class="person-first">Daniel</span>
      <span class="person-last">Hart</span>
      <span class="person-degree">(PhD)</span>
    </p>
    <p class="person-title">Managing Director</p>
  </main>
</body>
</html>
```